Brannigan Ashcroft LLC. custom built/handcrafted

I am recent small business owner looking to sell my art(drawings) and woodworking projects from my home. I have a very rough draft of a simple card design created on a simple digital program. I was hoping for a fancier lettering on the initial letters (BA). More of a calligraphy style. Also, the yellow border around the logo I would like to be a gold foil look. For it to be shiny or reflective look and to keep the other letters black with a consistent font on the card and the card white.

Target Market(s)

Local and neighboring cities

Industry/Entity Type

Art (drawing)/Woodworking

Contact Information for Business Card

My email tpashcroft@mailvane.net, phone number 949-517-3068. In the files provided it has a yellow border around the logo and I was looking to make that a gold foil.

Font styles to use
Serif
Decorative
Script

Requirements
Nice to have
• symbols for having a Facebook and Instagram

```html
<!DOCTYPE html>
<html lang="en">
<head>
<meta charset="utf-8">
<title>Brannigan Ashcroft – Business Card</title>
<link rel="stylesheet" href="https://fonts.googleapis.com/css2?family=Open+Sans:wght@400;700;800&display=swap">
<style>
  :root {
    --backdrop: #848589;
    --yellow: #f6c12b;
    --gold-dark: #d3a42c;
    --white: #ffffff;
    --grey-light: #e9eaec;
    --grey-line: #d1d2d4;
    --ink: #000000;
  }
  * { margin: 0; padding: 0; box-sizing: border-box; }
  html, body {
    width: 1200px;
    height: 1002px;
    overflow: hidden;
    background: var(--backdrop);
    font-family: "Open Sans", Arial, sans-serif;
    color: var(--ink);
  }
  .card {
    position: absolute;
    left: 253px;
    width: 694px;
    height: 397px;
    border-radius: 29px;
    overflow: hidden;
    background: var(--yellow);
  }
  .card--front { top: 66px; }
  .card--back { top: 539px; }
  .card__art {
    position: absolute;
    inset: 0;
    width: 100%;
    height: 100%;
    display: block;
  }
  .fill-yellow { fill: var(--yellow); }
  .fill-gold { fill: var(--gold-dark); }
  .fill-white { fill: var(--white); }
  .fill-grey { fill: var(--grey-light); }
  .stroke-grey { fill: none; stroke: var(--grey-line); stroke-width: 14; }

  .brand-mark {
    position: absolute;
    text-align: center;
    font-weight: 800;
    line-height: 1;
    white-space: nowrap;
  }
  .brand-mark__initials { display: block; letter-spacing: -2px; }
  .brand-mark__name { display: block; font-weight: 700; letter-spacing: 0.2px; }

  .card--front .brand-mark { left: 0; right: 0; top: 131px; }
  .card--front .brand-mark__initials { font-size: 138px; }
  .card--front .brand-mark__name { font-size: 19px; margin-top: 6px; }

  .tagline {
    position: absolute;
    right: 26px;
    top: 360px;
    font-size: 17px;
    font-weight: 700;
    letter-spacing: 0.3px;
  }

  .card--back .brand-mark { left: 485px; width: 140px; top: 102px; }
  .card--back .brand-mark__initials { font-size: 80px; }
  .card--back .brand-mark__name { font-size: 10px; margin-top: 3px; }

  .owner {
    position: absolute;
    left: 37px;
    top: 112px;
    width: 252px;
    text-align: center;
  }
  .owner__name { font-size: 26px; font-weight: 700; line-height: 1.1; letter-spacing: 0.2px; }
  .owner__role { font-size: 22px; font-weight: 400; line-height: 1.2; }

  .contact {
    position: absolute;
    left: 26px;
    top: 261px;
    list-style: none;
  }
  .contact__item {
    display: flex;
    align-items: center;
    gap: 6px;
    font-size: 22px;
    line-height: 29px;
  }
  .contact__icon { width: 24px; height: 24px; flex: none; }

  .social {
    position: absolute;
    left: 131px;
    top: 330px;
    display: flex;
    gap: 14px;
  }
  .social__badge {
    width: 32px;
    height: 32px;
    border-radius: 8px;
    background: var(--ink);
  }
</style>
</head>
<body>

<section class="card card--front">
  <svg class="card__art" viewBox="0 0 1214 694" preserveAspectRatio="none" aria-hidden="true">
    <rect class="fill-yellow" width="1214" height="694"/>
    <path class="fill-gold" d="M0,218 C250,230 500,120 850,22 C1000,12 1120,50 1214,85 V694 H0Z"/>
    <path class="fill-white" d="M0,262 C250,270 500,150 880,28 C1030,20 1130,60 1214,88 V694 H0Z"/>
    <path class="fill-grey" d="M380,212 C600,110 900,50 1214,148 V694 H0 V262 Z"/>
    <path class="stroke-grey" d="M470,172 C700,90 960,30 1214,150"/>
    <path class="fill-white" d="M0,335 C150,560 500,620 840,495 L1214,375 C1100,180 900,130 720,135 C560,140 430,190 370,215 L0,262 Z"/>
    <path class="stroke-grey" d="M0,562 C250,660 520,640 840,500"/>
    <path class="fill-white" d="M0,600 C250,680 520,660 840,520 L1214,400 V694 H0Z"/>
    <path class="fill-gold" d="M0,610 C250,690 500,690 800,560 C950,495 1100,428 1214,430 V694 H0Z"/>
    <path class="fill-yellow" d="M0,640 C250,700 520,700 830,582 C980,522 1120,470 1214,472 V694 H0Z"/>
  </svg>

  <div class="brand-mark">
    <span class="brand-mark__initials">BA</span>
    <span class="brand-mark__name">BRANNIGAN ASHCROFT</span>
  </div>
  <p class="tagline">CUSTOM BUILT·HANDCRAFTED</p>
</section>

<section class="card card--back">
  <svg class="card__art" viewBox="0 0 1214 694" preserveAspectRatio="none" aria-hidden="true">
    <rect class="fill-yellow" width="1214" height="694"/>
    <path class="fill-gold" d="M0,114 C200,140 450,110 640,0 H1214 V694 H0Z"/>
    <path class="fill-white" d="M0,120 C250,140 480,92 660,0 H1214 V694 H0Z"/>
    <path class="fill-grey" d="M470,80 C600,60 700,30 800,0 H700 C630,30 540,60 470,80Z"/>
    <path class="fill-yellow" d="M840,0 H1214 V145 C1100,20 900,10 680,45 C740,30 800,15 840,0Z"/>
    <path class="fill-grey" d="M680,45 C950,10 1170,90 1214,240 V145 C1110,30 900,15 680,45Z"/>
    <path class="fill-grey" d="M490,413 C720,470 920,580 1060,694 H1214 V390 C1100,520 900,510 690,470 Z"/>
    <path class="fill-white" d="M490,413 C700,480 880,590 1010,694 H880 C770,570 620,470 490,413Z"/>
    <path class="fill-yellow" d="M690,470 C850,530 1100,560 1214,460 V694 H1040 C950,600 820,520 690,470Z"/>
    <path class="fill-gold" d="M0,323 C420,320 720,480 850,694 H0Z"/>
    <path class="fill-yellow" d="M0,325 C360,330 650,480 800,694 H0Z"/>
  </svg>

  <div class="owner">
    <p class="owner__name">TOBIAS P. ASHCROFT</p>
    <p class="owner__role">OWNER</p>
  </div>

  <div class="brand-mark">
    <span class="brand-mark__initials">BA</span>
    <span class="brand-mark__name">BRANNIGAN ASHCROFT</span>
  </div>

  <ul class="contact">
    <li class="contact__item">
      <svg class="contact__icon" viewBox="0 0 24 24" aria-hidden="true">
        <circle cx="12" cy="12" r="12" fill="#000"/>
        <path d="M8.2,5.5 L10,8.8 L8.8,10.2 C9.6,12 11.3,13.8 13.3,14.8 L14.7,13.6 L18,15.4 L17,17.8 C12,18.4 5.6,12.2 6,7 Z" fill="#fff"/>
      </svg>
      <span>949-517-3068</span>
    </li>
    <li class="contact__item">
      <svg class="contact__icon" viewBox="0 0 24 24" aria-hidden="true">
        <circle cx="12" cy="12" r="12" fill="#000"/>
        <rect x="6" y="8" width="12" height="8.5" fill="none" stroke="#fff" stroke-width="1.3"/>
        <path d="M6,8 L12,13 L18,8" fill="none" stroke="#fff" stroke-width="1.3"/>
      </svg>
      <span>tpashcroft@mailvane.net</span>
    </li>
  </ul>

  <div class="social">
    <span class="social__badge" role="img" aria-label="Social profile link"></span>
    <span class="social__badge" role="img" aria-label="Social profile link"></span>
  </div>
</section>

</body>
</html>
```